velunique hair oil

Its an ayurvedic hair oil of 100 ml bottle. We need a design for the label. along with the wordings, some punch line too in the label. Mettalic silver bottle with black cap. Round bottle with height of 10 cm and width of 7 cm. The metallic silver colour bottle can be changed if some other nice colour combination is worked out

Target Market(s)

Retail, any one with a hair fall problem can be our target customer.. This ayurvedic hair oil is a miracle off sorts. With just one bottle hair fall totally stops and fresh hair grows.

Industry/Entity Type

Hair

Requirements
Must have
• HAVE WORDS 100% AYURVEDIC HAIR OIL IN A CIRCLE

MUST NOTE THAT THE BOTTLE IS ROUND
Nice to have
• Its for both men and women. Bottle is round in shape and hence the wording should be accordingly put
Should not have
• RED COLOUR.

```html
<!DOCTYPE html>
<html lang="en">
<head>
<meta charset="utf-8">
<title>Velunique Hair Oil – Label</title>
<link rel="stylesheet" href="https://fonts.googleapis.com/css2?family=Cinzel:wght@600&family=Roboto+Condensed:wght@300&family=Work+Sans:wght@300;400&display=swap">
<style>
  :root {
    --paper: #ffffff;
    --ink: #1f1f1f;
    --label-border: #e4e4e4;
    --leader: #b9b9b9;
    --gold-light: #f3ea8c;
    --gold-mid: #c9a443;
    --gold-dark: #8a6424;
  }
  * { margin: 0; padding: 0; box-sizing: border-box; }
  html, body { width: 1200px; height: 1000px; overflow: hidden; background: var(--paper); }
  .canvas { position: relative; width: 1200px; height: 1000px; color: var(--ink); font-family: "Work Sans", sans-serif; }

  .callout { position: absolute; top: 347px; font-size: 14px; font-weight: 400; letter-spacing: 0.2px; transform: translateX(-50%); white-space: nowrap; }
  .callout--back { left: 560px; }
  .callout--front { left: 909px; }
  .leaders { position: absolute; inset: 0; pointer-events: none; }

  .label { position: absolute; left: 358px; top: 409px; width: 745px; height: 375px; border: 3px solid var(--label-border); background: var(--paper); }

  .gold-foil { position: absolute; background: linear-gradient(100deg, var(--gold-light), var(--gold-mid) 45%, var(--gold-dark) 70%, var(--gold-light)); border-radius: 40% 60% 50% 50%; opacity: 0.9; }

  .brand { font-family: "Cinzel", serif; font-weight: 600; color: var(--ink); white-space: nowrap; }

  /* back panel */
  .back .gold-foil { left: 48px; top: 38px; width: 188px; height: 36px; }
  .back .brand { position: absolute; left: 118px; top: 82px; font-size: 22px; letter-spacing: 0.5px; }
  .ingredients { position: absolute; left: 35px; top: 130px; width: 250px; text-align: center; font-size: 13px; line-height: 19px; font-weight: 300; }
  .ingredients b { font-weight: 400; }
  .distributor { position: absolute; left: 10px; top: 298px; width: 300px; text-align: center; font-size: 15px; line-height: 23px; font-weight: 300; }

  /* front panel */
  .front .gold-foil { left: 497px; top: 20px; width: 62px; height: 312px; border-radius: 60% 20% 50% 40%; background: linear-gradient(180deg, var(--gold-mid), var(--gold-light) 40%, var(--gold-dark) 75%, var(--gold-light)); }
  .front .brand { position: absolute; left: 582px; top: 128px; font-size: 30px; letter-spacing: 1px; transform: translate(-50%, -50%) rotate(-90deg); }
  .claim { position: absolute; left: 619px; top: 111px; font-family: "Roboto Condensed", sans-serif; font-weight: 300; font-size: 19px; line-height: 25px; text-transform: uppercase; }
  .punchline { position: absolute; left: 586px; top: 243px; font-size: 17px; line-height: 22px; font-weight: 300; }
  .volume { position: absolute; left: 586px; top: 316px; font-size: 15px; font-weight: 300; }
</style>
</head>
<body>
<div class="canvas">
  <span class="callout callout--back">GOLD STAMPING</span>
  <span class="callout callout--front">GOLD STAMPING</span>
  <svg class="leaders" width="1200" height="1000" aria-hidden="true">
    <line x1="561" y1="368" x2="561" y2="443" stroke="var(--leader)" stroke-width="1"/>
    <line x1="909" y1="368" x2="909" y2="398" stroke="var(--leader)" stroke-width="1"/>
    <line x1="909" y1="398" x2="906" y2="420" stroke="var(--leader)" stroke-width="1"/>
  </svg>

  <div class="label">
    <section class="back">
      <div class="gold-foil" role="img" aria-label="Gold-stamped flowing hair strands"></div>
      <div class="brand">VELUNIQUE</div>
      <p class="ingredients"><b>INGREDIENTS:</b>Lorem ipsum dolor sit amet, consectetuer adipiscing elit, sed diam nonummy nibh euismod tincidunt ut laoreet dolore magna aliquam erat volutpat. Ut wisi enim ad minim veniam, quis nostrud exerci tation ullamcorper suscipit lobortis nisl ut aliquip ex ea commodo consequat.</p>
      <p class="distributor">Distruted By: Name of the company<br>www.velunique-care.com</p>
    </section>

    <section class="front">
      <div class="gold-foil" role="img" aria-label="Gold-stamped vertical hair strands"></div>
      <div class="brand">VELUNIQUE</div>
      <p class="claim">100%<br>Ayurvedic<br>Premium<br>Hair Oil</p>
      <p class="punchline">Fastest way to<br>stop hair fall</p>
      <p class="volume">100 mL</p>
    </section>
  </div>
</div>
</body>
</html>
```